Vending machine company website for SnackHarbor

We need a website for our vending machine services company. It will be based on another website that a friend has. My URL is snackharbor.com and the one I'm trying to emulate with my own logo and colors is pantrybloxo.com.

This will be roughly 6 total pages with one being an opt-in/opt-out page for SMS messages, one being a contact form, etc.

I want to use the logo I purchased from this site that I have attached.

The goal is to be clean, professional, intuitive and easy navigation, etc.

The only difference between my site and the reference site should be that we are not offering coffee service.

I will need all of the code for the site, and it should not use any CMS things like Joomla, Wordpress, etc.

Our actual machines are this model minus the green highlights.f

https://www.kelvomat.com/krx-pdl-mq-snack-and-drink-vending-machine-374.html

Target Market(s)

Companies that want to have vending machine services, or to buy or lease vending machines

Industry/Entity Type

Vending machines for snacks and drinks either placed at locations like apartment complexes, waiting rooms for tire centers, office building break rooms, etc. also vending machine repair services, or selling or leasing vending machines to those interested in getting into the business.

Coding

Coded - Design and coding required

Number of Pages Required

5+ page

Font styles to use
Sans Serif

Requirements
Must have
• It will be similar to pantrybloxo.com in terms of pages, categories, etc. but with our logo, colors, etc. and should be clean and professional. It will have the same pages plus one other page for opt-in or opt-out of SMS messages
Nice to have
• Clean graphics and perhaps some AI designs for vending machine repair, just like the one they use on the pantrybloxo.com site. We would like multiple photos on the home page cycling where you see very attractive people shopping for snacks and drinks at the machines with the items blurred, or people sitting around laughing and smiling while enjoying snacks or drinks at a campus break room, or picnic table, or outside with the machine behind them. Please search for KRX-PDL-47M(B2) Snack And Drink Vending Machine at kelvomat
Should not have
• It can not be designed for CRM like WordPress, Joomla, etc. and should be clean new code, that doesn't attract hackers and it shouldn't be too busy.

```html
<!DOCTYPE html>
<html lang="en">
<head>
<meta charset="utf-8">
<title>SnackHarbor — Vending Machines</title>
<link href="https://fonts.googleapis.com/css2?family=Urbanist:wght@700;800&family=Inter:wght@400;500;600;700&display=swap" rel="stylesheet">
<style>
:root{
  --red:#e32626;
  --red-deep:#c81c1c;
  --red-soft:#f25c5c;
  --orange:#ef9a2c;
  --ink:#1b1b1b;
  --text:#555;
  --dark:#0c0c0c;
  --cream:#fdf6ee;
  --blush:#fdf1f1;
  --white:#fff;
}
*{box-sizing:border-box;margin:0;padding:0}
html,body{width:1200px;height:5278px;overflow:hidden}
body{font-family:"Inter",sans-serif;color:var(--ink);background:var(--white);position:relative}
h1,h2,h3,h4,.brand{font-family:"Urbanist",sans-serif;font-weight:800}
.accent{color:var(--orange)}
section,header,footer{position:absolute;left:0;width:1200px}
.btn{position:absolute;display:flex;align-items:center;justify-content:center;background:var(--red);color:#fff;font-size:11px;font-weight:700;border-radius:2px}
.photo{position:absolute}
.drop{position:absolute;left:572px;width:56px;height:56px;border-radius:50%;display:flex;align-items:center;justify-content:center;z-index:3}
.drop svg{width:14px;height:40px}

/* hero */
.hero{top:0;height:710px;background:radial-gradient(ellipse at 50% 35%,#4a3a52 0%,#2a2230 45%,#111 100%)}
.hero .photo{inset:0;background:linear-gradient(90deg,#2b3d3a 0%,#4b2f44 25%,#5a2f4c 50%,#2e4f3d 72%,#223 100%);opacity:.55}
.hero .shade{position:absolute;inset:0;background:linear-gradient(180deg,rgba(0,0,0,.15) 0%,rgba(0,0,0,.35) 55%,rgba(0,0,0,.9) 100%)}
.nav{position:absolute;left:125px;top:30px;width:950px;height:70px;background:#fff;display:flex;align-items:center;padding:0 36px}
.brand{font-size:28px;color:var(--orange);font-weight:700}
.nav ul{list-style:none;display:flex;gap:36px;margin-left:110px;font-size:11px;font-weight:500}
.nav-cta{right:36px;top:17px;width:140px;height:36px}
.hero-title{position:absolute;top:322px;width:100%;text-align:center;color:#fff;font-size:44px;line-height:50px}
.hero-copy{position:absolute;top:440px;left:300px;width:600px;text-align:center;color:#eee;font-size:10.5px;line-height:21px}
.hero-cta{left:530px;top:528px;width:140px;height:34px}

/* about */
.about{top:710px;height:685px}
.about h2{position:absolute;left:748px;top:178px;font-size:34px}
.about p{position:absolute;left:748px;top:240px;width:280px;font-size:10.5px;line-height:21px;color:var(--text)}
.about .btn{left:748px;top:440px;width:140px;height:36px}

/* machines */
.machines{top:1395px;height:900px;background:linear-gradient(180deg,var(--red) 0%,var(--red-deep) 100%);color:#fff}
.machines h2{position:absolute;top:100px;width:100%;text-align:center;font-size:40px}
.machines .lede{position:absolute;top:160px;left:290px;width:620px;text-align:center;font-size:10.5px;line-height:21px}
.machine{position:absolute;top:250px;width:325px;text-align:center}
.machine .frame{height:392px;background:var(--red-soft);position:relative}
.machine .frame .photo{left:50px;top:40px;width:225px;height:320px;background:linear-gradient(180deg,#3a3a3a,#111);border-radius:4px}
.machine h3{margin-top:30px;font-size:24px}
.machine p{margin:14px auto 0;width:280px;font-size:10.5px;line-height:21px;color:#fde}
.cart{position:absolute;width:52px;height:52px;border-radius:50%;background:var(--orange);display:flex;align-items:center;justify-content:center}

/* services */
.services{top:2295px;height:480px}
.services h2{position:absolute;left:125px;top:168px;font-size:34px}
.services .copy{position:absolute;left:125px;top:228px;width:390px;font-size:10.5px;line-height:21px;color:var(--text)}
.svc{position:absolute;top:108px;width:239px;height:265px;border:1px solid #f2a0a0;border-radius:4px;text-align:center;padding:30px 26px 0}
.svc .ico{width:48px;height:48px;border-radius:50%;background:var(--red);margin:0 auto;display:flex;align-items:center;justify-content:center}
.svc h4{font-family:"Inter",sans-serif;font-weight:700;font-size:12.5px;margin-top:22px;line-height:18px}
.svc p{font-size:9.5px;line-height:18px;color:var(--text);margin-top:10px}

/* testimonials */
.clients{top:2775px;height:580px;background:radial-gradient(ellipse at 50% 50%,#2a231c 0%,#111 60%,#050505 100%)}
.clients .photo{inset:0;background:linear-gradient(90deg,#191a1a,#3b2c20 30%,#2e2418 70%,#141414);opacity:.55}
.clients h2{position:absolute;top:100px;width:100%;text-align:center;font-size:40px;color:#fff}
.clients .sub{position:absolute;top:168px;left:440px;width:320px;text-align:center;color:#ddd;font-size:10.5px;line-height:21px}
.quote{position:absolute;left:287px;top:245px;width:626px;height:210px;border:1px solid rgba(255,255,255,.35);background:rgba(255,255,255,.08);display:flex;align-items:center;justify-content:center;text-align:center;padding:0 60px;color:#fff;font-style:italic;font-size:13px;line-height:24px}
.arrow-btn{position:absolute;top:328px;width:26px;height:36px;border:1px solid #ccc;border-radius:4px;display:flex;align-items:center;justify-content:center}
.qmark{position:absolute;left:582px;top:440px;width:36px;height:36px;border-radius:50%;background:var(--red);display:flex;align-items:center;justify-content:center;color:#fff;font-family:"Urbanist",sans-serif;font-size:26px;line-height:1;padding-top:12px}

/* features */
.features{top:3355px;height:590px}
.features h2{position:absolute;left:125px;top:100px;font-size:34px}
.features .copy{position:absolute;left:125px;top:162px;width:640px;font-size:10.5px;line-height:21px;color:var(--text)}
.feat{position:absolute;top:260px;width:222px;height:225px;background:var(--cream);border:1px solid #e9b9a8;padding:30px 24px 0}
.feat .num{position:absolute;left:24px;top:-12px;width:26px;height:26px;border-radius:50%;background:#fff;border:1.5px solid var(--red);color:var(--red);font-size:9px;font-weight:700;display:flex;align-items:center;justify-content:center}
.feat h4{font-family:"Inter",sans-serif;font-weight:600;font-size:13px;line-height:22px}
.feat p{font-size:9.5px;line-height:18px;color:var(--text);margin-top:10px}

/* form */
.inquire{top:3945px;height:605px;background:linear-gradient(180deg,var(--red) 0%,var(--red-deep) 100%)}
.inquire h2{position:absolute;top:100px;width:100%;text-align:center;font-size:40px;color:#fff}
.field{position:absolute;height:45px;background:#fff;display:flex;align-items:center;padding-left:28px;font-size:12px;color:#999}
.send-btn{left:530px;top:470px;width:140px;height:35px;background:var(--orange)}

/* faq */
.faq{top:4550px;height:410px}
.faq h2{position:absolute;left:122px;top:125px;font-size:34px;line-height:42px}
.faq .copy{position:absolute;left:122px;top:232px;width:380px;font-size:10.5px;line-height:21px;color:var(--text)}
.acc{position:absolute;left:528px;width:547px;height:38px;background:var(--cream);border:1px solid #e79c8c;display:flex;align-items:center;justify-content:space-between;padding:0 24px;font-size:10px;font-weight:600}

/* footer */
.site-footer{top:4960px;height:245px;background:var(--blush)}
.site-footer .brand{position:absolute;left:125px;top:100px;font-size:46px}
.site-footer .rule{position:absolute;left:125px;top:160px;width:260px;height:1px;background:#888}
.contact{position:absolute;top:68px;width:200px;text-align:center;font-size:13px;line-height:22px}
.contact .ico{width:70px;height:70px;border-radius:50%;background:#fbe0dc;margin:0 auto 18px;display:flex;align-items:center;justify-content:center}
.divider{position:absolute;top:110px;width:1px;height:40px;background:#ccc}
.bottom{top:5205px;height:73px;background:var(--dark);color:#ddd;font-size:12px;display:flex;align-items:center;padding:0 125px;justify-content:space-between}
.socials{display:flex;gap:14px}
.socials span{width:16px;height:16px;border-radius:50%;background:#fff}
</style>
</head>
<body>

<header class="hero">
  <div class="photo" role="img" aria-label="Row of brightly lit snack and drink vending machines"></div>
  <div class="shade"></div>
  <nav class="nav">
    <span class="brand">SnackHarbor</span>
    <ul><li>About Us</li><li>Our Machines</li><li>Services</li><li>Products</li></ul>
    <span class="btn nav-cta">Contact Us</span>
  </nav>
  <h1 class="hero-title">Satisfy Your Cravings With<br><span class="accent">Every Click</span></h1>
  <p class="hero-copy">Lorem Ipsum is simply dummy text of the printing and typesetting industry. Lorem Ipsum has been the industry's standard dummy text ever since the 1500s, when an unknown printer took a galley of type and scrambled it to make a type specimen book.</p>
  <span class="btn hero-cta">Inquire Now</span>
  <div class="drop" style="top:682px;background:#000"><svg viewBox="0 0 14 40"><path d="M7 2v34M2 30l5 6 5-6" stroke="#fff" stroke-width="1.4" fill="none"/></svg></div>
</header>

<section class="about">
  <div class="photo" role="img" aria-label="Stocked snack vending machine" style="left:125px;top:107px;width:303px;height:470px;background:linear-gradient(180deg,#3a3a3a,#1d1d1d 60%,#555)"></div>
  <div class="photo" role="img" aria-label="Customer choosing a drink at a vending machine" style="left:448px;top:107px;width:172px;height:233px;background:linear-gradient(135deg,#d8d2c8,#8a8c90);border-right:10px solid var(--red)"></div>
  <div class="photo" role="img" aria-label="Technician restocking a vending machine" style="left:282px;top:360px;width:388px;height:182px;background:linear-gradient(90deg,#6f8c96,#3f5a4c 50%,#7a7a70);border:6px solid #fff"></div>
  <h2>About <span class="accent">Us</span></h2>
  <p>Lorem Ipsum is simply dummy text of the printing and typesetting industry. Lorem Ipsum has been the industry's standard dummy text ever since the 1500s, when an unknown printer took a galley of type and scrambled it to make a type specimen book. It has survived not only five centuries, but also the leap into electronic typesetting, remaining essentially unchanged.</p>
  <span class="btn">Read More</span>
</section>

<section class="machines">
  <div class="drop" style="top:-28px;background:var(--red)"><svg viewBox="0 0 14 40"><path d="M7 2v34M2 30l5 6 5-6" stroke="#fff" stroke-width="1.4" fill="none"/></svg></div>
  <h2>Our Vending <span class="accent">Machines</span></h2>
  <p class="lede">Lorem Ipsum is simply dummy text of the printing and typesetting industry. Lorem Ipsum has been the industry's standard dummy text ever since the 1500s,</p>
  <div class="machine" style="left:265px">
    <div class="frame"><div class="photo" role="img" aria-label="Compact combo snack and drink vending machine"></div></div>
    <h3>Compact Combo</h3>
    <p>Lorem Ipsum is simply dummy text of the printing and typesetting industry. Lorem Ipsum has been the industry's standard dummy text ever since the 1500s,</p>
  </div>
  <div class="machine" style="left:610px">
    <div class="frame"><div class="photo" role="img" aria-label="Standard combo snack and drink vending machine"></div></div>
    <h3>Standard Combo</h3>
    <p>Lorem Ipsum is simply dummy text of the printing and typesetting industry. Lorem Ipsum has been the industry's standard dummy text ever since the 1500s,</p>
  </div>
  <div class="cart" style="left:236px;top:276px"><svg width="22" height="22" viewBox="0 0 24 24" fill="none" stroke="var(--red)" stroke-width="2"><path d="M2 3h3l3 12h11l2-8H6"/><circle cx="9" cy="20" r="1.5"/><circle cx="18" cy="20" r="1.5"/></svg></div>
  <div class="cart" style="left:910px;top:276px"><svg width="22" height="22" viewBox="0 0 24 24" fill="none" stroke="var(--red)" stroke-width="2"><path d="M2 3h3l3 12h11l2-8H6"/><circle cx="9" cy="20" r="1.5"/><circle cx="18" cy="20" r="1.5"/></svg></div>
  <div class="drop" style="top:858px"><svg viewBox="0 0 14 40"><path d="M7 2v34M2 30l5 6 5-6" stroke="#fff" stroke-width="1.4" fill="none"/></svg></div>
</section>

<section class="services">
  <h2>Our <span class="accent">Services</span></h2>
  <p class="copy">Lorem Ipsum is simply dummy text of the printing and typesetting industry. Lorem Ipsum has been the industry's standard dummy text ever since the 1500s, when an unknown printer took a galley of type and scrambled it to make a type specimen book.</p>
  <div class="svc" style="left:580px">
    <div class="ico"><svg width="22" height="22" viewBox="0 0 24 24" fill="none" stroke="#fff" stroke-width="2"><path d="M14 6a4 4 0 0 0 5 5l-9 9-4-4 9-9z"/></svg></div>
    <h4>Vending Machine<br>Repairs</h4>
    <p>Lorem Ipsum is simply dummy text of the printing and typesetting industry. Lorem Ipsum has been the industry's standard dummy text ever since the 1500s,</p>
  </div>
  <div class="svc" style="left:838px">
    <div class="ico"><svg width="20" height="22" viewBox="0 0 20 24" fill="none" stroke="#fff" stroke-width="2"><rect x="3" y="2" width="14" height="20" rx="1"/><path d="M7 8h6M7 12h6M7 16h3"/></svg></div>
    <h4>Buy Or Leasing</h4>
    <p>Lorem Ipsum is simply dummy text of the printing and typesetting industry. Lorem Ipsum has been the industry's standard dummy text ever since the 1500s,</p>
  </div>
</section>

<section class="clients">
  <div class="photo" role="img" aria-label="Dimly lit wall of vending machines"></div>
  <div class="drop" style="top:-28px;background:#000"><svg viewBox="0 0 14 40"><path d="M7 2v34M2 30l5 6 5-6" stroke="#fff" stroke-width="1.4" fill="none"/></svg></div>
  <h2>What Our Clients <span class="accent">Says</span></h2>
  <p class="sub">Lorem Ipsum is simply dummy text of the printing and typesetting industry.</p>
  <div class="quote">Lorem Ipsum is simply dummy text of the printing and typesetting industry. Lorem Ipsum has been the industry's standard dummy text ever since the 1500s, when an unknown printer took a galley of type and scrambled it to make a type specimen book.</div>
  <div class="arrow-btn" style="left:250px"><svg width="8" height="14" viewBox="0 0 8 14"><path d="M7 1 1 7l6 6" stroke="#ddd" fill="none" stroke-width="1.5"/></svg></div>
  <div class="arrow-btn" style="left:924px"><svg width="8" height="14" viewBox="0 0 8 14"><path d="M1 1l6 6-6 6" stroke="#ddd" fill="none" stroke-width="1.5"/></svg></div>
  <div class="qmark">”</div>
  <div class="drop" style="top:552px;background:#000"><svg viewBox="0 0 14 40"><path d="M7 2v34M2 30l5 6 5-6" stroke="#fff" stroke-width="1.4" fill="none"/></svg></div>
</section>

<section class="features">
  <h2>Features &amp; <span class="accent">Benefits</span></h2>
  <p class="copy">Lorem Ipsum is simply dummy text of the printing and typesetting industry. Lorem Ipsum has been the industry's standard dummy text ever since the 1500s,</p>
  <div class="feat" style="left:125px"><span class="num">01</span><h4>Lorem Ipsum is simply dummy text</h4><p>Lorem Ipsum is simply dummy text of the printing and typesetting industry. Lorem Ipsum has been the industry's standard dummy text ever since the 1500s,</p></div>
  <div class="feat" style="left:368px"><span class="num">02</span><h4>Lorem Ipsum is simply dummy text</h4><p>Lorem Ipsum is simply dummy text of the printing and typesetting industry. Lorem Ipsum has been the industry's standard dummy text ever since the 1500s,</p></div>
  <div class="feat" style="left:610px"><span class="num">03</span><h4>Lorem Ipsum is simply dummy text</h4><p>Lorem Ipsum is simply dummy text of the printing and typesetting industry. Lorem Ipsum has been the industry's standard dummy text ever since the 1500s,</p></div>
  <div class="feat" style="left:853px"><span class="num">04</span><h4>Lorem Ipsum is simply dummy text</h4><p>Lorem Ipsum is simply dummy text of the printing and typesetting industry. Lorem Ipsum has been the industry's standard dummy text ever since the 1500s,</p></div>
</section>

<section class="inquire">
  <div class="drop" style="top:-28px;background:var(--red)"><svg viewBox="0 0 14 40"><path d="M7 2v34M2 30l5 6 5-6" stroke="#fff" stroke-width="1.4" fill="none"/></svg></div>
  <h2>Need A Vending <span class="accent">Machine?</span></h2>
  <div class="field" style="left:223px;top:197px;width:372px">First name</div>
  <div class="field" style="left:605px;top:197px;width:372px">Last name</div>
  <div class="field" style="left:223px;top:258px;width:754px">Email address</div>
  <div class="field" style="left:223px;top:319px;width:754px">Phone</div>
  <div class="field" style="left:223px;top:380px;width:754px">Organization name and a brief description about you...</div>
  <span class="btn send-btn">Send</span>
  <div class="drop" style="top:560px"><svg viewBox="0 0 14 40"><path d="M7 2v34M2 30l5 6 5-6" stroke="#fff" stroke-width="1.4" fill="none"/></svg></div>
</section>

<section class="faq">
  <h2>Frequently Asked<br><span class="accent">Questions</span></h2>
  <p class="copy">Lorem Ipsum is simply dummy text of the printing and typesetting industry. Lorem Ipsum has been the industry's standard dummy text ever since the 1500s,</p>
  <div class="acc" style="top:110px">Lorem Ipsum is simply dummy text?<svg width="10" height="6"><path d="M0 0h10L5 6z" fill="#333"/></svg></div>
  <div class="acc" style="top:165px">Lorem Ipsum is simply dummy text of the printing?<svg width="10" height="6"><path d="M0 0h10L5 6z" fill="#333"/></svg></div>
  <div class="acc" style="top:218px">Lorem Ipsum is simply dummy text?<svg width="10" height="6"><path d="M0 0h10L5 6z" fill="#333"/></svg></div>
  <div class="acc" style="top:272px">Lorem Ipsum is simply dummy text of the printing?<svg width="10" height="6"><path d="M0 0h10L5 6z" fill="#333"/></svg></div>
</section>

<footer class="site-footer">
  <span class="brand">SnackHarbor</span>
  <span class="rule"></span>
  <div class="contact" style="left:460px">
    <div class="ico"><svg width="22" height="22" viewBox="0 0 24 24"><path d="M6 2l4 4-2 3a12 12 0 0 0 7 7l3-2 4 4-3 3C10 21 3 14 3 5z" fill="var(--orange)"/></svg></div>
    Phone:<br>(833) 555-0142
  </div>
  <div class="divider" style="left:662px"></div>
  <div class="contact" style="left:685px">
    <div class="ico"><svg width="24" height="20" viewBox="0 0 24 20"><rect x="2" y="4" width="20" height="14" rx="2" fill="var(--orange)"/><path d="M2 6l10 7 10-7" stroke="#fff" stroke-width="1.6" fill="none"/></svg></div>
    Email address:<br>info@pantrybloxo.com
  </div>
  <div class="divider" style="left:905px"></div>
  <div class="contact" style="left:915px">
    <div class="ico"><svg width="22" height="22" viewBox="0 0 24 24"><path d="M22 2 2 10l9 3 3 9z" fill="var(--orange)"/></svg></div>
    Location:<br>San Francisco, CA
  </div>
</footer>

<footer class="bottom">
  <span>© Copyright 2023 SNACKHARBOR. All rights reserved</span>
  <div class="socials"><span></span><span></span><span></span><span></span><span></span></div>
</footer>

</body>
</html>
```